Business card and company stationary - Bravora Cleaning Ltd

1. Who are we and who are our customers?

o We are a relatively new cleaning company, established December 2008. We are a small company. We have 24 staff and we offer domestic and commercial cleaning services.
o We both (me and my wife) have been working for many years in the cleaning industry. We worked for some of the biggest and best cleaning companies in UK. We’ve been operatives, supervisors and managers.
o Inevitably after so many years of working for someone else, we decided to start our own business.
o Our domestic customers are middle class families and busy professionals. We’ve got some commercial customers, mainly offices.
o We are growing steadily.

2. What do we do? What are our services?

o Cleaning. We’ve got range of services - not to many but still can be daunting and confusing for some.
o Generally we’ve got domestic and commercial clients. The approach to the domestic cleaning customers is different to the commercial. In the way we want to say that it is cleaning that we do, but we acknowledge the environment and we appreciate the personal circumstances and requirements that are present. We do care, we listen and we try to work out the best possible way to complete our work.
o Mainly we get our work through referrals

3. What do we want with our stationery ?

o To place and maintain our message and reach out to people and organisations
o We want to advertise, communicate and sale.
o We are going to sell services.
o Increase membership, loyalty and support.

We are after business card design, headed letter and compliment slip.
We would like the headed letter to be created in formats suitable for :
- printing format
- also for use in our daily correspondence via e mail with clients and staff in a easy to edit and write format

The website we have is still under contraction and the domain is bravoracleaning.example

Target Market(s)

Families, individuals, businesses.

Industry/Entity Type

Cleaning Service

Contact Information for Business Card

FRONT :
Company Name - Bravora Cleaning Ltd
Company address - 41 Pelgate Rd, Larkmoor, Wendshire, LK14 7QD
Name - Mrs. Radoslava Petkova - Sola
Title - Managing Director
Company phone - 020 8937 2158
E mail - sola.petkova@bravoracleaning.example

BACK :

Company website - bravoracleaning.example
E mail - enquiries@bravoracleaning.example

Font styles to use
Serif

Requirements
Must have
• The above items and company logo...maybe at the back. But I'm free for any suggestions.

```html
<!DOCTYPE html>
<html lang="en">
<head>
<meta charset="utf-8">
<title>Bravora Cleaning Ltd – Letterhead</title>
<link rel="stylesheet" href="https://fonts.googleapis.com/css2?family=Libre+Franklin:wght@400;500&display=swap">
<style>
  :root {
    --paper: #ffffff;
    --ink: #1a1a1a;
    --ink-soft: #4a4a4a;
    --rule: #5bbfe6;
    --brand: #3cb4e5;
  }
  html, body {
    margin: 0;
    padding: 0;
    overflow: hidden;
    background: var(--paper);
  }
  .letterhead {
    position: relative;
    width: 932px;
    height: 1200px;
    background: var(--paper);
    font-family: "Libre Franklin", Arial, sans-serif;
    color: var(--ink-soft);
    overflow: hidden;
  }
  .brand {
    position: absolute;
    top: 40px;
    left: 688px;
    width: 200px;
    display: flex;
    flex-direction: column;
    align-items: center;
    gap: 12px;
  }
  .brand-dot {
    width: 104px;
    height: 104px;
    border-radius: 50%;
    background: var(--brand);
  }
  .brand-name {
    font-size: 18px;
    font-weight: 500;
    color: var(--ink);
    letter-spacing: 0.4px;
    white-space: nowrap;
  }
  .footer {
    position: absolute;
    left: 72px;
    right: 68px;
    top: 1067px;
  }
  .website {
    text-align: center;
    font-size: 16px;
    letter-spacing: 2.6px;
    color: var(--ink);
    margin: 0 0 8px;
  }
  .footer-rule {
    height: 0;
    border-top: 1.5px solid var(--rule);
    margin: 0 0 10px;
  }
  .contact {
    display: flex;
    font-size: 16px;
    line-height: 24px;
  }
  .address { width: 306px; margin: 0; font-style: normal; }
  .phones { width: 207px; }
  .contact-line {
    display: flex;
    align-items: center;
    gap: 9px;
    white-space: nowrap;
  }
  .contact-line svg { flex: none; fill: var(--ink); }
  .emails { font-size: 15.5px; }
  .emails .contact-line { gap: 10px; }
</style>
</head>
<body>
<main class="letterhead">
  <header class="brand">
    <div class="brand-dot"></div>
    <div class="brand-name">Bravora Cleaning Ltd</div>
  </header>

  <footer class="footer">
    <p class="website">www.bravoracleaning.example</p>
    <div class="footer-rule"></div>
    <div class="contact">
      <address class="address">41 Pelgate Rd.<br>Larkmoor, Wendshire, LK14 7QD</address>
      <div class="phones">
        <div class="contact-line">
          <svg width="14" height="20" viewBox="0 0 14 20" aria-hidden="true"><path d="M2 0h10a2 2 0 0 1 2 2v16a2 2 0 0 1-2 2H2a2 2 0 0 1-2-2V2a2 2 0 0 1 2-2zm0 3v12h10V3zm5 13.2a1.2 1.2 0 1 0 0 2.4a1.2 1.2 0 0 0 0-2.4z"/></svg>
          <span>078 5512 3047</span>
        </div>
        <div class="contact-line">
          <svg width="18" height="16" viewBox="0 0 18 16" aria-hidden="true"><path d="M1 4c0-2 3-3 8-3s8 1 8 3v1.5h-4V4H5v1.5H1zM4 7h10l3 5v4H1v-4zm5 2a2.5 2.5 0 1 0 0 5a2.5 2.5 0 0 0 0-5z"/></svg>
          <span>020 8937 2158</span>
        </div>
      </div>
      <div class="emails">
        <div class="contact-line">
          <svg width="18" height="13" viewBox="0 0 18 13" aria-hidden="true"><path d="M0 0h18v2l-9 5-9-5zm0 4l9 5 9-5v9H0z"/></svg>
          <span>accounts@bravoracleaning.example</span>
        </div>
        <div class="contact-line">
          <svg width="18" height="13" viewBox="0 0 18 13" aria-hidden="true"><path d="M0 0h18v2l-9 5-9-5zm0 4l9 5 9-5v9H0z"/></svg>
          <span>enquiries@bravoracleaning.example</span>
        </div>
      </div>
    </div>
  </footer>
</main>
</body>
</html>
```